Financial Markets Algorithmic Trading solution needs One pager Marketing designs

We are creating Marketing sheets that will be handed to potential clients that will give a broad base of our products available. We are an established Sell side firm in the financial Industry and our product focus is a Technology base solution and we want to showcases our Algorithmic trading suite.
Our customer base is Buy-side Traders,hedge funds, managing directors. We want a clean high end technology based look that will encompass the colors that are in our logo.
We intend to work with the designer after initial design to encompass the theme to other pages we have. So we will need a design that can be part of a set but can stand alone.

** i have uploaded a new File that is the correct File to design to. Please follow the flow of the categories and what resides under those headers. This is key for the delivery of the material****

Target Market(s)

Finance- Buy side firms, geared for meetings and info sheets to be left with clients who are CEO's , Head Traders, Managing Directors

Industry/Entity Type

Financial Service

Font styles to use
Other font styles liked:
• Tw Cen MT

Requirements
Must have
• Must include the logo, and encompass the colors that are in the logo.
• We want this to have a Technology company feel to it. We would like it clean and unique, all while not falling into the normal classic business look.
• Also for this page we would like to keep the layout similar to what we have.
• Please keep the style of lettering
Should not have
• Messy look, overpowering color. no cartoon graphics

```html
<!DOCTYPE html>
<html lang="en">
<head>
<meta charset="utf-8">
<title>Algorithmic Trading Strategy Overview</title>
<link href="https://fonts.googleapis.com/css2?family=Oswald:wght@400;500;600&family=Questrial&display=swap" rel="stylesheet">
<style>
  :root{
    --backdrop:#e9e7e4;
    --paper:#ffffff;
    --orange:#ef7d2c;
    --blue:#1a7dc3;
    --ink:#1f1f1f;
    --muted:#555;
    --photo-a:#dfe6ec;
    --photo-b:#9fb0bf;
  }
  *{box-sizing:border-box;margin:0;padding:0}
  html,body{width:1200px;height:1000px;overflow:hidden;background:var(--backdrop)}
  .sheet{position:absolute;left:246px;top:42px;width:708px;height:916px;background:var(--paper);box-shadow:0 4px 14px rgba(0,0,0,.18);font-family:"Questrial",sans-serif;color:var(--ink);overflow:hidden}
  .hero-photo{position:absolute;left:0;top:0;width:708px;height:420px;background:linear-gradient(135deg,var(--photo-a) 0%,#c7d2dc 45%,var(--photo-b) 100%)}
  .hero-fade{position:absolute;left:0;top:340px;width:708px;height:90px;background:linear-gradient(rgba(255,255,255,0),#fff)}
  .brand{position:absolute;left:420px;top:290px;display:flex;align-items:center;gap:10px}
  .brand-mark{width:14px;height:14px;background:var(--blue)}
  .brand-name{font-family:"Questrial",sans-serif;font-size:22px;color:var(--blue)}
  .title-banner{position:absolute;left:76px;top:386px;width:556px;height:34px}
  .title-banner svg{position:absolute;inset:0;width:100%;height:100%}
  .title-banner h1{position:relative;font-family:"Oswald",sans-serif;font-weight:500;font-size:25px;letter-spacing:.3px;color:#fff;text-align:center;line-height:34px}
  .intro{position:absolute;left:44px;top:430px;width:622px;font-size:11.9px;line-height:16.6px;text-align:justify;color:var(--ink)}
  .strategies{position:absolute;left:0;top:563px;width:708px;height:278px;background:var(--blue);color:#fff}
  .col{position:absolute;top:10px;width:182px}
  .col:nth-child(1){left:56px}
  .col:nth-child(2){left:264px}
  .col:nth-child(3){left:472px}
  .category{font-family:"Oswald",sans-serif;font-weight:500;font-size:17px;color:#e4f1fb;line-height:22px}
  .strategy{margin-top:2px}
  .strategy + .strategy{margin-top:18px}
  .strategy h3{font-family:"Oswald",sans-serif;font-weight:400;font-size:12.5px;line-height:17px}
  .strategy p{font-size:9.3px;line-height:12px;margin-top:3px}
  .footnote{position:absolute;right:52px;bottom:16px;font-size:9.5px}
  .rule{position:absolute;left:0;width:708px;background:var(--blue)}
  .rule.one{top:843px;height:4px}
  .rule.two{top:850px;height:2px}
  .contact{position:absolute;left:82px;top:864px}
  .contact .label{font-size:11px;letter-spacing:.3px}
  .contact .name{font-family:"Oswald",sans-serif;font-weight:600;font-size:18px;letter-spacing:.6px;line-height:22px}
  .address{position:absolute;left:290px;top:862px;width:370px;text-align:center;font-size:13px}
  .links{position:absolute;left:290px;top:881px;width:370px;display:flex;justify-content:center;align-items:center;gap:6px;font-size:12.5px;color:var(--muted)}
  .links svg{width:11px;height:11px;vertical-align:-1px}
  .sep{color:var(--blue)}
</style>
</head>
<body>
  <main class="sheet">
    <div class="hero-photo" role="img" aria-label="Photo of a trader wearing a headset at a desk with several monitors showing trading screens"></div>
    <div class="hero-fade"></div>
    <div class="brand"><span class="brand-mark"></span><span class="brand-name">Brightwell &amp; Partners</span></div>

    <div class="title-banner">
      <svg viewBox="0 0 556 34" preserveAspectRatio="none"><polygon points="0,0 556,0 544,17 556,34 0,34 12,17" fill="var(--orange)"/></svg>
      <h1>ALGORITHMIC TRADING STRATEGY OVERVIEW</h1>
    </div>

    <p class="intro">Brightwell &amp; Partners has partnered with an award winning algorithmic trading platform and developed a custom suite of algorithms designed to ensure high quality execution.&nbsp; Our algorithms incorporate our unique ATX point of sale order types (pQuote* / rQuote*) seamlessly into each strategy.&nbsp; This integration smooth's workflow, improves execution quality, ensures greater liquidity sourcing, minimizes information leakage and brings a wide variety of Algo and SOR strategies directly into your OMS, EMS, or proprietary trading platform.&nbsp; In addition, we work in a consultative role to develop custom DMA routes, design algorithms according to client needs or specific requirements, and implement unique routing strategies designed to efficiently touch today's complex market micro-strategy.</p>

    <section class="strategies">
      <div class="col">
        <h2 class="category">Liquidity Sourcing</h2>
        <div class="strategy">
          <h3>SOR*</h3>
          <p>Optimizes order placement in lit and dark venues to maximize liquidity capture and minimize information leakage. The strategy balances "Urgency to capture the display quote" vs. opportunities to seek out dark liquidity to minimize information leakage and price</p>
        </div>
        <div class="strategy">
          <h3>DARK AGG</h3>
          <p>Manages orderplacement in darkvenues to optimize liquidity capture and reduce information leakage. The strategy attempts to first discover liquidity by slicing optimally sized orders at various venues, and then rebalances intelligently to venues where it has detected liquidity.</p>
        </div>
      </div>
      <div class="col">
        <h2 class="category">Schedule Driven</h2>
        <div class="strategy">
          <h3>VWAP*</h3>
          <p>Trades using historical volume profile to target VWAP as the benchmark. The strategy can optionally accept StartTime and EndTime as parameters to schedule trading in a given trading period. The strategy utilizes passive and aggressive trading tactics to achieve liquidity.</p>
        </div>
        <div class="strategy">
          <h3>TWAP*</h3>
          <p>Similar to the VWAP strategy with a different schedule. The schedule is a constant rate of trading between the given StartTime and EndTime.</p>
        </div>
      </div>
      <div class="col">
        <h2 class="category">Dynamic &amp; Adaptive</h2>
        <div class="strategy">
          <h3>POV*</h3>
          <p>Tracks volume from the time the order starts trading and trades according to the specified target participation percentage. Continuous optimizations are made as the order trades to target optima price and liquidity goals.</p>
        </div>
        <div class="strategy">
          <h3>ARRIVAL PRICE*</h3>
          <p>Manages the trade-off between market impact and volatility (price risk) to optimally execute the order.</p>
        </div>
      </div>
      <p class="footnote">*Indicates pQuote/ rQuote</p>
    </section>
    <div class="rule one"></div>
    <div class="rule two"></div>

    <div class="contact">
      <p class="label">CONTACT:</p>
      <p class="name">DANA WHITLOCK</p>
    </div>
    <p class="address">48 Harbor Lane, New York, NY 10004</p>
    <p class="links">
      <span><svg viewBox="0 0 12 12"><rect x="3" y="0.5" width="6" height="11" rx="1.2" fill="none" stroke="var(--blue)" stroke-width="1.2"/></svg> 212.555.0147</span>
      <span class="sep">|</span>
      <span><svg viewBox="0 0 12 12"><rect x="0.6" y="2" width="10.8" height="8" fill="none" stroke="var(--blue)" stroke-width="1.1"/><polyline points="0.6,2 6,6.5 11.4,2" fill="none" stroke="var(--blue)" stroke-width="1.1"/></svg> info@brightwell.com</span>
      <span class="sep">|</span>
      <span><svg viewBox="0 0 12 12"><circle cx="6" cy="6" r="5.2" fill="none" stroke="var(--blue)" stroke-width="1.1"/><ellipse cx="6" cy="6" rx="2.2" ry="5.2" fill="none" stroke="var(--blue)" stroke-width="1"/><line x1="0.8" y1="6" x2="11.2" y2="6" stroke="var(--blue)" stroke-width="1"/></svg> www.brightwell.com</span>
    </p>
  </main>
</body>
</html>
```